Thank you cards for online orders

We have a logo that is attached and I'd for it to be used to make a thank you card that will give our clients some info on product care as well as refund/exchange policy. so maybe a small package that includes a thank you card, and policy details
Updates

Sick

Target Market(s)

Females for 20-70

```html
<!DOCTYPE html>
<html lang="en">
<head>
<meta charset="utf-8">
<title>Velara – Thank You Card</title>
<link href="https://fonts.googleapis.com/css2?family=Raleway:wght@400;500;700&display=swap" rel="stylesheet">
<style>
  :root {
    --teal: #138e96;
    --paper: #efeded;
    --white: #ffffff;
    --green: #5a9e2e;
  }
  * { margin: 0; padding: 0; box-sizing: border-box; }
  html, body { width: 849px; height: 1200px; overflow: hidden; background: var(--paper); }
  .card {
    position: relative;
    width: 849px;
    height: 1200px;
    overflow: hidden;
    background: var(--paper);
    font-family: "Raleway", sans-serif;
  }
  .honeycomb, .pennant { position: absolute; left: 0; top: 0; }
  .cell-frame { fill: none; stroke: var(--teal); stroke-width: 18; stroke-linejoin: miter; }
  .cell-blank { fill: var(--white); stroke: var(--teal); stroke-width: 18; stroke-linejoin: miter; }
  .brand {
    position: absolute;
    left: 91px; width: 665px; top: 38px;
    text-align: center;
    color: var(--white);
    font-weight: 400;
    font-size: 46px;
    letter-spacing: 11px;
    text-indent: 11px;
  }
  .headline {
    position: absolute;
    left: 91px; width: 665px; top: 138px;
    text-align: center;
    color: var(--white);
    font-weight: 700;
    font-size: 47px;
    letter-spacing: 2px;
  }
  .cell-label {
    position: absolute;
    text-align: center;
    color: var(--teal);
    font-weight: 700;
    font-size: 29px;
    line-height: 1.12;
    letter-spacing: 0.5px;
  }
  .message-title { left: 298px; width: 260px; top: 584px; }
  .message-body {
    position: absolute;
    left: 318px; width: 220px; top: 634px;
    text-align: center;
    color: var(--green);
    font-weight: 400;
    font-size: 29px;
    line-height: 1.17;
    letter-spacing: 0.5px;
  }
  .refund-title { left: 38px; width: 260px; top: 1018px; }
  .contacts-title { left: 560px; width: 260px; top: 1034px; }
</style>
</head>
<body>
<main class="card">
  <svg class="honeycomb" width="849" height="1200" viewBox="0 0 849 1200">
    <defs>
      <linearGradient id="tone-neck" x1="0" y1="0" x2="1" y2="1">
        <stop offset="0" stop-color="#d2a88c"/>
        <stop offset="0.55" stop-color="#b07a5b"/>
        <stop offset="1" stop-color="#9aa7ad"/>
      </linearGradient>
      <linearGradient id="tone-veil" x1="0" y1="0" x2="1" y2="1">
        <stop offset="0" stop-color="#6f4d3c"/>
        <stop offset="0.5" stop-color="#c0896b"/>
        <stop offset="1" stop-color="#f0d3cf"/>
      </linearGradient>
      <linearGradient id="tone-silver" x1="0" y1="0" x2="1" y2="1">
        <stop offset="0" stop-color="#4f3f36"/>
        <stop offset="0.5" stop-color="#b7927a"/>
        <stop offset="1" stop-color="#a9cbd6"/>
      </linearGradient>
      <linearGradient id="tone-portrait" x1="0" y1="0" x2="1" y2="1">
        <stop offset="0" stop-color="#ebe8e6"/>
        <stop offset="0.45" stop-color="#c99e84"/>
        <stop offset="1" stop-color="#7d6a60"/>
      </linearGradient>
      <linearGradient id="tone-red" x1="0" y1="0" x2="1" y2="1">
        <stop offset="0" stop-color="#efc9c6"/>
        <stop offset="0.45" stop-color="#b98467"/>
        <stop offset="1" stop-color="#c2232b"/>
      </linearGradient>
      <radialGradient id="glint" cx="0.5" cy="0.62" r="0.45">
        <stop offset="0" stop-color="#e8cf8e" stop-opacity="0.55"/>
        <stop offset="1" stop-color="#e8cf8e" stop-opacity="0"/>
      </radialGradient>
    </defs>

    <g role="img" aria-label="Photo: gold and turquoise beaded necklace worn on the neck">
      <polygon fill="url(#tone-neck)" points="327,535 244,679 78,679 -5,535 78,391 244,391"/>
      <polygon fill="url(#glint)" points="327,535 244,679 78,679 -5,535 78,391 244,391"/>
      <polygon class="cell-frame" points="327,535 244,679 78,679 -5,535 78,391 244,391"/>
    </g>
    <g role="img" aria-label="Photo: model in bridal veil wearing a kundan necklace and earrings">
      <polygon fill="url(#tone-veil)" points="861,535 778,679 612,679 529,535 612,391 778,391"/>
      <polygon fill="url(#glint)" points="861,535 778,679 612,679 529,535 612,391 778,391"/>
      <polygon class="cell-frame" points="861,535 778,679 612,679 529,535 612,391 778,391"/>
    </g>
    <g role="img" aria-label="Photo: layered kundan choker worn with a light blue outfit">
      <polygon fill="url(#tone-silver)" points="327,842 244,986 78,986 -5,842 78,698 244,698"/>
      <polygon fill="url(#glint)" points="327,842 244,986 78,986 -5,842 78,698 244,698"/>
      <polygon class="cell-frame" points="327,842 244,986 78,986 -5,842 78,698 244,698"/>
    </g>
    <g role="img" aria-label="Photo: model wearing a statement necklace and drop earrings">
      <polygon fill="url(#tone-portrait)" points="861,842 778,986 612,986 529,842 612,698 778,698"/>
      <polygon fill="url(#glint)" points="861,842 778,986 612,986 529,842 612,698 778,698"/>
      <polygon class="cell-frame" points="861,842 778,986 612,986 529,842 612,698 778,698"/>
    </g>
    <g role="img" aria-label="Photo: model in red blouse wearing a green stone necklace">
      <polygon fill="url(#tone-red)" points="594,995 511,1139 345,1139 262,995 345,851 511,851"/>
      <polygon fill="url(#glint)" points="594,995 511,1139 345,1139 262,995 345,851 511,851"/>
      <polygon class="cell-frame" points="594,995 511,1139 345,1139 262,995 345,851 511,851"/>
    </g>

    <polygon class="cell-blank" points="594,688 511,832 345,832 262,688 345,544 511,544"/>
    <polygon class="cell-blank" points="327,1149 244,1293 78,1293 -5,1149 78,1005 244,1005"/>
    <polygon class="cell-blank" points="861,1149 778,1293 612,1293 529,1149 612,1005 778,1005"/>
    <polygon class="cell-blank" points="594,1302 511,1446 345,1446 262,1302 345,1158 511,1158"/>
  </svg>

  <svg class="pennant" width="849" height="360" viewBox="0 0 849 360" aria-hidden="true">
    <polygon points="91,0 756,0 756,155 424,345 91,155" fill="var(--teal)"/>
    <polyline points="105,0 105,147 424,329 742,147 742,0" fill="none" stroke="var(--white)" stroke-width="3"/>
  </svg>

  <div class="brand">VELARA</div>
  <h1 class="headline">THANK YOU</h1>

  <h2 class="cell-label message-title">Message</h2>
  <p class="message-body">Message for the product goes here.</p>

  <h2 class="cell-label refund-title">Refund<br>Policy</h2>
  <h2 class="cell-label contacts-title">Contacts</h2>
</main>
</body>
</html>
```